QBoost480 Business Card Design

I am in need of a business card design.

Business Name: Quantum Boost 480 or Qboost480 (we can try the business card with both variations)

I would like it to be somewhat different from the "average" business card

What do we do?

We link up with distributors of different items and we Market their products, sell their products, fulfill the shipment, and handle all customer service that goes along with it.

I will be uploading our logo as well as other business card ideas that i have seen and liked on the web.

I like the style of the "graphic design" business card that i uploaded. I was thinking maybe something like that but instead would read.

SYNC | SELL | SHIP

With maybe:
a computer or a Sync icon underneath SYNC
Some form of money sign underneath Sell
a delivery truck or something underneath SHIP.

And then I was thinking maybe put the logo on the back side like in the other business card that i uploaded.

I definitely want a double sided business card.

These are only my suggestions and if i was very confident in my idea then I wouldn't have to be on here. (So make what you think is nice because my opinion is probably not so great anyway!!)

Everything can be changed.

ALSO, For the logo
We can try and remove the text multi channel selling

For the Business card contact info:
Milo Quenton
CEO
2914 Ravensby Street
J7T-2K8
Montreal, Quebec

Thanks

Target Market(s)

Businesses

Industry/Entity Type

Information Technology

Font styles to use
Serif
Sans Serif
Decorative

Colors
34a6d6
33b8a4
aaaaaa
85cae6
33a6d7
0492cd
9d9d9d

Requirements
Must have
• Double Sided Business card
Nice to have
• Illustration graphics / Icons underneath the main points

```html
<!DOCTYPE html>
<html lang="en">
<head>
<meta charset="utf-8">
<title>QBoost480 Business Card</title>
<link rel="stylesheet" href="https://fonts.googleapis.com/css2?family=Fira+Sans+Condensed:wght@300;400;600&display=swap">
<style>
  :root {
    --page-bg: #e9e6e1;
    --card-bg: #ffffff;
    --brand-blue: #0492cd;
    --name-blue: #34a6d6;
    --text-grey: #555555;
    --label-grey: #6f6f6f;
    --rule-grey: #9d9d9d;
    --deco-grey: #ececec;
    --sync-green: #7cc242;
    --sell-grey: #e4e4e4;
    --ship-blue: #1e9fe0;
  }
  * { margin: 0; padding: 0; box-sizing: border-box; }
  html, body {
    width: 1200px; height: 1023px; overflow: hidden;
    background: var(--page-bg);
    font-family: "Fira Sans Condensed", "Arial Narrow", sans-serif;
  }
  .card {
    position: absolute; left: 120px; top: 237px;
    width: 960px; height: 548px;
    background: var(--card-bg);
    box-shadow: 0 6px 24px rgba(0,0,0,0.12);
  }
  .card__decoration {
    position: absolute; left: 30px; top: 40px;
    width: 330px; height: 330px; border-radius: 50%;
    background: radial-gradient(circle, var(--deco-grey) 0%, rgba(236,236,236,0.4) 60%, rgba(255,255,255,0) 75%);
  }
  .brand {
    position: absolute; left: 48px; top: 400px;
    display: flex; align-items: center; gap: 14px;
  }
  .brand__dot {
    width: 22px; height: 22px; border-radius: 50%;
    background: var(--brand-blue);
  }
  .brand__name {
    font-size: 60px; font-weight: 600; color: var(--brand-blue);
    letter-spacing: -0.5px;
  }
  .divider-vertical {
    position: absolute; width: 2px; background: var(--rule-grey);
  }
  .divider-vertical--brand { left: 392px; top: 290px; height: 150px; }
  .divider-vertical--services { left: 690px; top: 58px; height: 290px; }
  .divider-horizontal {
    position: absolute; left: 420px; top: 470px;
    width: 480px; height: 2px; background: var(--rule-grey);
  }
  .contact__name {
    position: absolute; left: 420px; top: 170px;
    font-size: 44px; font-weight: 300; color: var(--name-blue);
  }
  .contact__role {
    position: absolute; left: 420px; top: 226px;
    font-size: 27px; font-weight: 300; color: var(--name-blue);
  }
  .contact__address {
    position: absolute; left: 420px; top: 290px;
    font-size: 31px; font-weight: 300; color: var(--text-grey);
    line-height: 48px; font-style: normal;
  }
  .services { position: absolute; left: 710px; top: 58px; width: 210px; }
  .service {
    display: flex; align-items: center; justify-content: space-between;
    height: 96px; padding-right: 6px;
  }
  .service__label {
    font-size: 29px; font-weight: 300; color: var(--label-grey);
    letter-spacing: 0.5px;
  }
  .service__icon { width: 66px; height: 66px; }
</style>
</head>
<body>
  <main class="card">
    <div class="card__decoration" role="img" aria-label="Faint grey network illustration of linked nodes"></div>

    <div class="brand">
      <span class="brand__dot"></span>
      <span class="brand__name">QBoost480</span>
    </div>

    <span class="divider-vertical divider-vertical--brand"></span>

    <h1 class="contact__name">Milo Quenton</h1>
    <p class="contact__role">CEO</p>
    <address class="contact__address">
      2914 Ravensby Street<br>
      J7T-2K8<br>
      Montreal, Quebec
    </address>

    <span class="divider-vertical divider-vertical--services"></span>

    <ul class="services" style="list-style:none">
      <li class="service">
        <span class="service__label">SYNC</span>
        <svg class="service__icon" viewBox="0 0 66 66" aria-hidden="true">
          <circle cx="33" cy="33" r="33" fill="var(--sync-green)"/>
          <rect x="18" y="17" width="30" height="22" rx="2" fill="#3d5a6c"/>
          <rect x="21" y="20" width="24" height="16" fill="#bfe3f2"/>
          <rect x="29" y="39" width="8" height="6" fill="#3d5a6c"/>
          <rect x="23" y="45" width="20" height="3" rx="1" fill="#3d5a6c"/>
        </svg>
      </li>
      <li class="service">
        <span class="service__label">SELL</span>
        <svg class="service__icon" viewBox="0 0 66 66" aria-hidden="true">
          <circle cx="33" cy="33" r="33" fill="var(--sell-grey)"/>
          <rect x="16" y="22" width="34" height="22" rx="2" fill="#5bb56a" transform="rotate(-12 33 33)"/>
          <circle cx="33" cy="33" r="6" fill="#e9f6ea"/>
          <text x="33" y="37" font-size="10" text-anchor="middle" fill="#3a8a48" font-family="Arial, sans-serif">$</text>
        </svg>
      </li>
      <li class="service">
        <span class="service__label">SHIP</span>
        <svg class="service__icon" viewBox="0 0 66 66" aria-hidden="true">
          <circle cx="33" cy="33" r="33" fill="var(--ship-blue)"/>
          <rect x="14" y="24" width="24" height="16" rx="1" fill="#6b6b6b"/>
          <path d="M38 28 h8 l6 7 v5 h-14 z" fill="#d9534f"/>
          <circle cx="22" cy="42" r="4" fill="#333"/>
          <circle cx="45" cy="42" r="4" fill="#333"/>
        </svg>
      </li>
    </ul>

    <span class="divider-horizontal"></span>
  </main>
</body>
</html>
```